Women's Health Company needs business card

We need a business card for a USA based women's health care company. We use digital technology to enhance therapy prescribed by clinicians for their patients

```html
<!DOCTYPE html>
<html lang="en">
<head>
<meta charset="utf-8">
<title>Lunova Health – Business Card</title>
<link rel="stylesheet" href="https://fonts.googleapis.com/css2?family=Roboto:wght@400;500;700&display=swap">
<style>
  :root {
    --backdrop: #bcbdc0;
    --paper: #ffffff;
    --teal: #74c0bc;
    --purple: #9154a0;
    --white: #ffffff;
  }
  * { margin: 0; padding: 0; box-sizing: border-box; }
  html, body {
    width: 962px;
    height: 1200px;
    overflow: hidden;
    background: var(--backdrop);
    font-family: "Roboto", Arial, sans-serif;
  }
  .card {
    position: absolute;
    left: 27px;
    width: 904px;
    height: 543px;
    overflow: hidden;
  }
  .card--front { top: 40px; background: var(--paper); }
  .card--back { top: 616px; background: var(--purple); }

  .wave { position: absolute; inset: 0; width: 100%; height: 100%; }

  .brand {
    position: absolute;
    display: flex;
    align-items: center;
    gap: 12px;
    font-weight: 500;
    color: var(--teal);
    white-space: nowrap;
  }
  .brand__dot { border-radius: 50%; flex: none; }
  .card--front .brand { left: 62px; top: 100px; font-size: 46px; }
  .card--front .brand__dot { width: 14px; height: 14px; background: var(--purple); }
  .card--back .brand {
    left: 50%; top: 50%;
    transform: translate(-50%, -50%);
    font-size: 56px;
  }
  .card--back .brand__dot { width: 16px; height: 16px; background: var(--white); }

  .person { position: absolute; left: 62px; top: 284px; }
  .person__name {
    font-size: 38px; font-weight: 700; color: var(--teal);
    letter-spacing: -0.5px; line-height: 1;
  }
  .person__title {
    margin-top: 14px;
    font-size: 24px; font-weight: 400; color: var(--purple); line-height: 1;
  }

  .contact { position: absolute; color: var(--purple); font-size: 21px; letter-spacing: 0.3px; line-height: 1; }
  .contact--address { left: 513px; top: 278px; }
  .contact--address .icon { position: absolute; left: 0; top: 0; width: 36px; height: 56px; }
  .contact--address p { margin-left: 51px; margin-top: 3px; }
  .contact--address p + p { margin-top: 16px; }

  .contact-list { position: absolute; left: 513px; top: 384px; list-style: none; }
  .contact-list li { display: flex; align-items: center; height: 22px; margin-bottom: 13px; color: var(--purple); font-size: 21px; letter-spacing: 0.3px; }
  .contact-list .icon { width: 26px; height: 22px; margin-right: 13px; flex: none; }
</style>
</head>
<body>

<section class="card card--front">
  <svg class="wave" viewBox="0 0 904 543" aria-hidden="true">
    <path fill="var(--teal)" d="M150,543 C300,480 370,360 430,290 C530,170 650,110 760,112 C830,113 880,125 904,132 L904,147 C870,136 820,127 760,128 C660,130 550,185 452,300 C385,382 320,480 172,543 Z"/>
  </svg>

  <div class="brand"><span class="brand__name">Lunova Health</span><span class="brand__dot"></span></div>

  <div class="person">
    <p class="person__name">NAME XXXXXXX</p>
    <p class="person__title">TITLE XXXXXXXX</p>
  </div>

  <div class="contact contact--address">
    <svg class="icon" viewBox="0 0 36 56" aria-hidden="true">
      <path fill="var(--teal)" d="M18 0C8 0 0 8 0 18c0 12 18 38 18 38s18-26 18-38C36 8 28 0 18 0z"/>
      <circle cx="18" cy="17" r="7" fill="var(--paper)"/>
    </svg>
    <p>XXXXXXXXXXX</p>
    <p>XXXXXXXXXXXXXXXXXX</p>
  </div>

  <ul class="contact-list">
    <li>
      <svg class="icon" viewBox="0 0 26 22" aria-hidden="true">
        <path fill="var(--teal)" d="M1 6c2-4 22-4 24 0v3h-6V6H7v3H1z"/>
        <path fill="var(--teal)" d="M6 10h14l2 11H4z"/>
        <circle cx="13" cy="15" r="3" fill="var(--paper)"/>
      </svg>
      <span>XXXXXXXXXX</span>
    </li>
    <li>
      <svg class="icon" viewBox="0 0 26 22" aria-hidden="true">
        <path fill="var(--teal)" d="M5 2h14l6 9-9 10H3l4-8z"/>
        <path fill="none" stroke="var(--paper)" stroke-width="1.5" d="M7 13l18-2"/>
      </svg>
      <span>XXXXXXXXXXXXXXXXX</span>
    </li>
    <li>
      <svg class="icon" viewBox="0 0 26 22" aria-hidden="true">
        <g fill="none" stroke="var(--teal)" stroke-width="1.6">
          <circle cx="13" cy="11" r="9.5"/>
          <ellipse cx="13" cy="11" rx="4.5" ry="9.5"/>
          <path d="M3.5 11h19M5 6h16M5 16h16M13 1.5v19"/>
        </g>
      </svg>
      <span>XXXXXXXXXXXXXXXX</span>
    </li>
  </ul>
</section>

<section class="card card--back">
  <div class="brand"><span class="brand__name">Lunova Health</span><span class="brand__dot"></span></div>
</section>

</body>
</html>
```